A5 Flyer for Financial Services Business

I am after a re-design of our business flyer to fit in with our new branding style and logo colour scheme. Wanting something with a bit of designer flair that I could not create myself. I have included the flyer which I created which lacks style so dazzle me.

I want to use the same content.

Text for main body of flyer is

Are you a small business owner, tradie or PAVC Service Provider struggling to stay on top of your bookkeeping and compliance obligations? If so we would love to help you get back on track and take control of your business finances so that you can make informed business decisions and focus on what you do best.

We have over 20 years industry experience and, as a small business ourselves, we are able to offer our clients a personal bookkeeping solution tailored to meet the needs of your business.

Accounts Payable | Accounts Receivable
Customer Invoicing
Bank and Credit Card Reconciliations
Payroll | Superannuation | Payroll Tax
Business Activity | Instalment Activity Statements
Regular Financial Reports
Xero and Quickbooks Set-Up and Training

```html
<!DOCTYPE html>
<html lang="en">
<head>
<meta charset="utf-8">
<title>Even Keel Financial Services – Flyer</title>
<link href="https://fonts.googleapis.com/css2?family=Open+Sans:wght@400;600;700&family=Montserrat:wght@500;600;700&display=swap" rel="stylesheet">
<style>
  :root {
    --page-bg: #e6e6e6;
    --paper: #ffffff;
    --teal: #17868c;
    --teal-dark: #0d5a62;
    --teal-light: #2aa6a6;
    --ink: #5a5a5a;
    --ink-dark: #333333;
    --band-grey: #6b6b6b;
    --photo-deep: #5d6d7c;
    --photo-mid: #9aa6b0;
    --photo-light: #eef1f2;
  }
  * { margin: 0; padding: 0; box-sizing: border-box; }
  html, body { width: 900px; height: 1200px; overflow: hidden; }
  body {
    background: var(--page-bg);
    font-family: "Open Sans", Arial, sans-serif;
    color: var(--ink-dark);
    position: relative;
  }
  .flyer {
    position: absolute;
    left: 38px; top: 15px;
    width: 824px; height: 1170px;
    background: var(--paper);
    overflow: hidden;
    box-shadow: 0 4px 14px rgba(0,0,0,.18);
  }
  .flyer-shapes { position: absolute; inset: 0; }
  .brand {
    position: absolute; right: 44px; top: 96px;
    display: flex; align-items: center; gap: 12px;
  }
  .brand-mark { width: 34px; height: 34px; background: var(--teal); }
  .brand-name {
    font-family: "Montserrat", Arial, sans-serif;
    font-weight: 500; font-size: 24px; color: var(--teal);
    letter-spacing: .5px;
  }
  .column { position: absolute; text-align: center; }
  .column-experience { left: 30px; top: 578px; width: 360px; }
  .column-audience { left: 420px; top: 478px; width: 376px; }
  .kicker {
    font-family: "Montserrat", Arial, sans-serif;
    font-weight: 500; font-size: 25px; color: var(--ink-dark);
    letter-spacing: .5px; line-height: 1.1;
  }
  .headline-years {
    font-family: "Montserrat", Arial, sans-serif;
    font-weight: 600; font-size: 62px; color: var(--teal);
    line-height: 1.05;
  }
  .headline-small {
    font-family: "Montserrat", Arial, sans-serif;
    font-weight: 700; font-size: 33px; color: var(--teal);
    line-height: 1.1;
  }
  .headline-owner {
    font-family: "Montserrat", Arial, sans-serif;
    font-weight: 600; font-size: 80px; color: var(--ink);
    line-height: 1; letter-spacing: 1px;
  }
  .lead {
    font-family: "Montserrat", Arial, sans-serif;
    font-weight: 500; font-size: 17px; color: var(--ink-dark);
    line-height: 1.2; margin-top: 8px;
  }
  .body-copy {
    font-size: 14px; line-height: 1.4; color: var(--ink-dark);
    margin-top: 12px;
  }
  .column-audience .body-copy { text-align: left; margin-top: 22px; }
  .service-list {
    list-style: none; text-align: left; margin-top: 30px;
  }
  .column-audience .service-list { margin-top: 16px; }
  .service-list li {
    display: flex; align-items: center; gap: 16px;
    font-size: 14px; font-weight: 600; color: var(--ink-dark);
    height: 44px;
  }
  .service-icon { width: 24px; height: 24px; flex: none; }
  .column-divider {
    position: absolute; left: 400px; top: 800px;
    width: 1px; height: 175px; background: #b8b8b8;
  }
  .web-address {
    position: absolute; right: 60px; top: 1112px;
    font-size: 18px; color: #ffffff; letter-spacing: .3px;
  }
</style>
</head>
<body>
<div class="flyer">
  <svg class="flyer-shapes" width="824" height="1170" viewBox="0 0 824 1170">
    <defs>
      <linearGradient id="photoTone" x1="0" y1="0" x2="0.3" y2="1">
        <stop offset="0" stop-color="var(--photo-light)"/>
        <stop offset="0.35" stop-color="var(--photo-mid)"/>
        <stop offset="1" stop-color="var(--photo-deep)"/>
      </linearGradient>
      <linearGradient id="softPanel" x1="0" y1="0" x2="0" y2="1">
        <stop offset="0" stop-color="#e6e6e6"/>
        <stop offset="1" stop-color="#ffffff"/>
      </linearGradient>
      <linearGradient id="tealBand" x1="0" y1="0" x2="1" y2="1">
        <stop offset="0" stop-color="var(--teal-light)"/>
        <stop offset="1" stop-color="var(--teal)"/>
      </linearGradient>
      <linearGradient id="tealDeep" x1="0" y1="0" x2="1" y2="0">
        <stop offset="0" stop-color="var(--teal)"/>
        <stop offset="1" stop-color="var(--teal-dark)"/>
      </linearGradient>
      <linearGradient id="silver" x1="0" y1="0" x2="1" y2="0">
        <stop offset="0" stop-color="#ffffff"/>
        <stop offset="1" stop-color="#bdbdbd"/>
      </linearGradient>
    </defs>

    <!-- hero image area -->
    <polygon points="0,0 824,0 824,335 0,515" fill="url(#photoTone)"
             role="img" aria-label="Photo of a businessman in a suit drawing a market line chart, blended with a city skyline"/>

    <!-- grey accent band above the headline -->
    <polygon points="424,458 824,352 824,420 540,462" fill="var(--band-grey)"/>

    <!-- light panel behind the headlines -->
    <polygon points="0,560 424,470 824,430 824,690 0,690" fill="url(#softPanel)"/>
    <polygon points="0,528 440,505 0,566" fill="#cfcfcf"/>

    <!-- faint city backdrop behind the copy -->
    <rect x="0" y="690" width="824" height="320" fill="#f4f5f5"
          role="img" aria-label="Faint city skyline photo behind the text"/>

    <!-- bottom bands -->
    <polygon points="0,1010 300,1090 0,1130" fill="url(#tealBand)"/>
    <polygon points="0,1130 300,1090 824,1050 824,1170 0,1170" fill="url(#tealDeep)"/>
    <polygon points="190,1128 560,1086 330,1160" fill="url(#silver)"/>
    <polygon points="580,1042 824,1002 824,1050 720,1072" fill="var(--teal)"/>
  </svg>

  <div class="brand">
    <span class="brand-mark"></span>
    <span class="brand-name">EVEN KEEL Financial Services</span>
  </div>

  <section class="column column-audience">
    <p class="kicker">ARE YOU A</p>
    <p class="headline-small">SMALL BUSINESS</p>
    <h1 class="headline-owner">OWNER</h1>
    <p class="lead">tradie or PAVC Service Provider struggling to stay on top of your bookkeeping and compliance obligations?</p>
    <p class="body-copy">If so we would love to help you get back on track and take control of your business finances so that you can make informed business decisions and focus on what you do best.</p>
    <ul class="service-list">
      <li><svg class="service-icon" viewBox="0 0 24 24"><rect x="2" y="2" width="20" height="20" rx="3" fill="var(--teal)"/><path d="M7 12l3.5 3.5L17 9" stroke="#fff" stroke-width="2.4" fill="none"/></svg>Accounts Payable | Accounts Receivable</li>
      <li><svg class="service-icon" viewBox="0 0 24 24"><rect x="2" y="2" width="20" height="20" rx="3" fill="var(--teal)"/><path d="M7 12l3.5 3.5L17 9" stroke="#fff" stroke-width="2.4" fill="none"/></svg>Customer Invoicing</li>
      <li><svg class="service-icon" viewBox="0 0 24 24"><rect x="2" y="2" width="20" height="20" rx="3" fill="var(--teal)"/><path d="M7 12l3.5 3.5L17 9" stroke="#fff" stroke-width="2.4" fill="none"/></svg>Bank and Credit Card Reconciliations</li>
      <li><svg class="service-icon" viewBox="0 0 24 24"><rect x="2" y="2" width="20" height="20" rx="3" fill="var(--teal)"/><path d="M7 12l3.5 3.5L17 9" stroke="#fff" stroke-width="2.4" fill="none"/></svg>Payroll | Superannuation | Payroll Tax</li>
    </ul>
  </section>

  <section class="column column-experience">
    <p class="kicker">WE HAVE OVER</p>
    <h2 class="headline-years">20 YEARS</h2>
    <p class="body-copy">industry experience and, as a small business ourselves, we are able to offer our clients a personal bookkeeping solution tailored to meet the needs of your business.</p>
    <ul class="service-list">
      <li><svg class="service-icon" viewBox="0 0 24 24"><rect x="2" y="2" width="20" height="20" rx="3" fill="var(--teal)"/><path d="M7 12l3.5 3.5L17 9" stroke="#fff" stroke-width="2.4" fill="none"/></svg>Accounts Payable | Accounts Receivable</li>
      <li><svg class="service-icon" viewBox="0 0 24 24"><rect x="2" y="2" width="20" height="20" rx="3" fill="var(--teal)"/><path d="M7 12l3.5 3.5L17 9" stroke="#fff" stroke-width="2.4" fill="none"/></svg>Customer Invoicing</li>
      <li><svg class="service-icon" viewBox="0 0 24 24"><rect x="2" y="2" width="20" height="20" rx="3" fill="var(--teal)"/><path d="M7 12l3.5 3.5L17 9" stroke="#fff" stroke-width="2.4" fill="none"/></svg>Bank and Credit Card Reconciliations</li>
      <li><svg class="service-icon" viewBox="0 0 24 24"><rect x="2" y="2" width="20" height="20" rx="3" fill="var(--teal)"/><path d="M7 12l3.5 3.5L17 9" stroke="#fff" stroke-width="2.4" fill="none"/></svg>Payroll | Superannuation | Payroll Tax</li>
    </ul>
  </section>

  <div class="column-divider"></div>

  <p class="web-address">www.evenkeelbooks.com.au</p>
</div>
</body>
</html>
```